New Zealand Export company needs business cards

We need new business cards to match our new logo for a company based in New Zealand who deal specifically with the Pacific Islands. We source, consolidate and ship products out of New Zealand to the Pacific Islands. Will attach our old ones and also new logo.
Would like the Islands we deal with and the areas of work we have access to, to be included on the business cards.

Contact Information for Business Card

T +64 9 571 3048
F +64 9 571 6285
12-18 Kowhai Lane, Drury, 2113
PO Box 814, Drury, Auckland 2247, New Zealand
www.falconfreight.example.nz
E sales@falconfreight.example.nz

Font styles to use
Sans Serif

Colors
85abd2
33a6d7
ffffff

Requirements
Must have
• A company of PWM

```html
<!DOCTYPE html>
<html lang="en">
<head>
<meta charset="utf-8">
<title>Falcon Freight – Business Card</title>
<link href="https://fonts.googleapis.com/css2?family=Arimo:wght@400;700&display=swap" rel="stylesheet">
<style>
  :root {
    --backdrop: #2e5258;
    --card: #ffffff;
    --ink: #1b55a0;
    --brand-dark: #1d5aa6;
    --accent: #33a6d7;
    --muted: #85abd2;
    --rule: #8fb0d0;
  }
  * { margin: 0; padding: 0; box-sizing: border-box; }
  html, body { width: 1200px; height: 1000px; overflow: hidden; }
  body {
    background: var(--backdrop);
    font-family: "Arimo", Arial, sans-serif;
    position: relative;
  }
  .card {
    position: absolute;
    left: 75px; top: 212px;
    width: 1050px; height: 600px;
    background: var(--card);
    box-shadow: 0 6px 18px rgba(0,0,0,.35);
  }
  .brand {
    position: absolute;
    left: 63px; top: 66px;
    display: flex; align-items: center; gap: 16px;
  }
  .brand-square {
    width: 58px; height: 58px;
    background: var(--accent);
  }
  .brand-name {
    font-weight: 700;
    font-size: 40px;
    letter-spacing: 2px;
    line-height: 1;
    color: var(--brand-dark);
    text-transform: uppercase;
  }
  .parent-company {
    position: absolute;
    left: 143px; top: 170px;
    font-size: 27px;
    color: var(--muted);
  }
  .address {
    position: absolute;
    left: 60px; top: 383px;
  }
  .address .pin { position: absolute; left: 0; top: 2px; }
  .address p {
    margin-left: 57px;
    font-size: 27px;
    line-height: 35px;
    color: var(--ink);
  }
  .address p + p { margin-top: 35px; }
  .divider {
    position: absolute;
    left: 574px; top: 225px;
    width: 2px; height: 172px;
    background: var(--rule);
  }
  .contacts {
    position: absolute;
    left: 600px; top: 215px;
    list-style: none;
  }
  .contacts li {
    display: flex; align-items: center;
    height: 48px;
    font-size: 27px;
    color: var(--ink);
  }
  .contacts li:last-child { margin-top: 6px; }
  .contacts svg { width: 26px; height: 26px; margin-right: 28px; flex: none; }
  .icon { fill: none; stroke: var(--accent); stroke-width: 1.8; stroke-linecap: round; stroke-linejoin: round; }
</style>
</head>
<body>
  <section class="card">
    <div class="brand">
      <span class="brand-square"></span>
      <span class="brand-name">Falcon Freight</span>
    </div>
    <p class="parent-company">A Company of PWM</p>

    <div class="address">
      <svg class="pin" width="26" height="34" viewBox="0 0 26 34" aria-hidden="true">
        <path d="M13 0C6 0 1 5 1 12c0 8 12 22 12 22s12-14 12-22C25 5 20 0 13 0z" fill="var(--accent)"/>
        <circle cx="13" cy="12" r="4.5" fill="#fff"/>
      </svg>
      <p>12-18 Kowhai Lane,<br>Drury, 2113</p>
      <p>PO Box 814, Drury,<br>Auckland 2247, New Zealand</p>
    </div>

    <span class="divider"></span>

    <ul class="contacts">
      <li>
        <svg viewBox="0 0 26 26" aria-hidden="true"><path class="icon" d="M6 3l4 5-2 3c1 3 4 6 7 7l3-2 5 4-2 4C12 24 2 14 2 5z"/><path class="icon" d="M15 4a7 7 0 0 1 7 7M15 8a3 3 0 0 1 3 3"/></svg>
        +64 9 571 3048
      </li>
      <li>
        <svg viewBox="0 0 26 26" aria-hidden="true"><rect class="icon" x="3" y="9" width="6" height="15"/><rect class="icon" x="9" y="11" width="14" height="13"/><path class="icon" d="M11 11V3h9v8M13 15h1M17 15h1M13 19h1M17 19h1"/></svg>
        Fax: +64 9 571 6285
      </li>
      <li>
        <svg viewBox="0 0 26 26" aria-hidden="true"><path class="icon" d="M3 11v13h20V11M3 11l10 8 10-8M3 24l8-6M23 24l-8-6"/><circle class="icon" cx="13" cy="8" r="4"/></svg>
        sales@falconfreight.example.nz
      </li>
      <li>
        <svg viewBox="0 0 26 26" aria-hidden="true"><circle class="icon" cx="13" cy="13" r="11"/><ellipse class="icon" cx="13" cy="13" rx="5" ry="11"/><path class="icon" d="M2 13h22M4 7h18M4 19h18"/></svg>
        www.falconfreight.example.nz
      </li>
    </ul>
  </section>
</body>
</html>
```